Tri-fold Brochure Design for Law Firm

I need a tri-fold brochure to give to prospective clients.
I have attached a Photoshop design file of a tri-fold brochure. The content (copy) is good, however, he brochure itself looks very amateurish.
I want a professional, sophisticated looking brochure.
The law firm specializes in commercial debt collection.
The law firm is located in New York City.
Our target market is business owners, doctors, lawyers, collection agencies and accountants.
Visit my website which is being designed at www.dornvek.com. I like the font used for the name of my company and the rich blue color used.

Target Market(s)

Business Owners, Doctors, Law Firms and Accountants

Industry/Entity Type

Law Firm

Font styles to use
Serif

Requirements
Must have
• Professional quality graphic work. Attention to details.
• PHOTOGRAPHS ONLY, NO CLIP-ART.
• DARK COLORS - NAVY BLUE, HUNTER GREEN, BLACK, GRAY & WHITE
Nice to have
• I want it to look smart, modern and sophisticated.
• Visit my website which is being designed at www.dornvek.com. I like the font used for the name of my company and the rich blue color used.
Should not have
• Bad artwork
• CLIP ART

```html
<!DOCTYPE html>
<html lang="en">
<head>
<meta charset="utf-8">
<title>Arturo Dornvek &amp; Company — Tri-fold Brochure</title>
<link href="https://fonts.googleapis.com/css2?family=Rajdhani:wght@500;600;700&family=Raleway:ital,wght@0,400;0,500;0,600;0,700;1,600&display=swap" rel="stylesheet">
<style>
:root{
  --backdrop:#8c8c8c;
  --navy:#1a55a6;
  --navy-deep:#0f458f;
  --navy-soft:#1d5cad;
  --green:#17a585;
  --green-bright:#27bb93;
  --ink:#1d4f9d;
  --body:#5e5e5e;
  --paper:#ffffff;
  --stone-light:#e4e4e2;
  --stone-dark:#a9aaa8;
}
*{box-sizing:border-box;margin:0;padding:0}
html,body{width:1200px;height:1200px;overflow:hidden;background:var(--backdrop)}
.stage{position:absolute;left:0;top:0;width:1500px;height:1500px;transform:scale(.8);transform-origin:0 0;
  background:radial-gradient(circle at 50% 45%,#9a9a9a,#848484);font-family:"Raleway",sans-serif}
.sheet{position:absolute;overflow:hidden;background:var(--paper);box-shadow:0 2px 6px rgba(0,0,0,.25)}
.sheet-outside{left:172px;top:84px;width:857px;height:662px}
.sheet-inside{left:172px;top:753px;width:857px;height:662px}
.sheet-cover-a{left:1042px;top:84px;width:287px;height:662px}
.sheet-cover-b{left:1042px;top:753px;width:287px;height:662px}
.panel{position:absolute;top:0;width:287px;height:662px}
.panel-art{position:absolute;left:0;top:0;width:100%;height:100%}
.abs{position:absolute}
.icon{display:inline-block;vertical-align:middle}

/* ---------- back panel ---------- */
.back-panel{left:0;width:283px;color:#fff}
.rule-heading{position:absolute;left:20px;width:244px;font-family:"Rajdhani",sans-serif;font-weight:700;font-size:21px;
  line-height:20px;color:var(--green-bright);text-transform:uppercase;padding-left:6px;padding-bottom:1px;
  border-left:1px solid rgba(255,255,255,.55);border-bottom:1px solid rgba(255,255,255,.55)}
.copy{position:absolute;left:20px;width:244px;font-size:9.6px;line-height:13px;text-align:justify;color:#fff}
.copy p+p{margin-top:6px}
.accent-line{position:absolute;left:20px;width:244px;font-size:12.5px;line-height:17px;color:var(--green-bright);text-transform:uppercase}
.serve-title{position:absolute;left:20px;top:200px;font-size:12px;font-weight:700;color:var(--green-bright)}
.check-list{position:absolute;list-style:none;font-size:9.4px;line-height:13.4px}
.check-list li{position:relative;padding-left:15px;margin-bottom:4px}
.check-list li svg{position:absolute;left:0;top:2px;width:10px;height:10px}
.serve-a{left:20px;top:218px;width:120px}
.serve-b{left:147px;top:218px;width:120px}
.why-list{left:20px;top:442px;width:250px}
.why-list li{padding-left:19px;margin-bottom:5px}

/* ---------- contact panel ---------- */
.seal{left:84px;top:191px;width:112px;height:112px;border-radius:50%;border:5px solid #fff;
  background:radial-gradient(circle at 45% 40%,#f2b35c,#c56c25 55%,#6d3412)}
.firm-name{left:0;width:287px;text-align:center;font-family:"Rajdhani",sans-serif;font-weight:700;text-transform:uppercase}
.firm-name small{font-size:.3em;letter-spacing:.5px}
.contact-name{top:309px;font-size:23px;line-height:19px;color:var(--ink)}
.tagline{left:0;top:350px;width:287px;text-align:center;font-size:10px;font-style:italic;font-weight:600;color:#fff}
.hair{left:45px;top:369px;width:196px;height:1px;background:rgba(255,255,255,.85)}
.principal{left:0;top:373px;width:287px;text-align:center;font-family:"Rajdhani",sans-serif;font-weight:600;font-size:13px;color:var(--ink)}
.principal-role{left:0;top:387px;width:287px;text-align:center;font-size:6.8px;color:#fff}
.reach{left:0;top:397px;width:287px;text-align:center;font-size:8.6px;color:#fff}
.reach .icon{width:9px;height:9px;margin:0 2px 1px 6px}
.mail-label{left:0;top:421px;width:287px;text-align:center;font-size:7.6px;font-weight:700;color:var(--ink)}
.mail-lines{left:0;top:432px;width:287px;text-align:center;font-size:7.6px;line-height:11.5px;color:#fff;text-transform:uppercase}
.branch{left:32px;top:509px;width:240px;color:var(--body)}
.branch-title{font-size:8.8px;font-weight:700;color:var(--ink);text-transform:uppercase}
.branch-title .icon{width:12px;height:12px;margin-right:3px}
.branch-lines{padding-left:16px;font-size:8.6px;line-height:11.4px;text-transform:uppercase;margin-top:1px}
.branch-phones{padding-left:0;font-family:"Rajdhani",sans-serif;font-weight:600;font-size:14.5px;color:var(--ink);margin-top:4px}
.branch-phones .icon{width:12px;height:12px;margin:0 2px 2px 0}
.branch-web{font-size:11px;color:var(--body)}
.branch-web .icon{width:11px;height:11px;margin:0 2px 2px 0}
.branch-web b{color:var(--ink)}
.tollfree{left:33px;top:603px;width:221px;height:33px;border:1.5px solid var(--ink);display:flex;align-items:center;justify-content:center;
  font-family:"Rajdhani",sans-serif;font-weight:600;font-size:27px;color:var(--ink)}
.tollfree .icon{width:22px;height:22px;margin-right:6px}
.tollfree-label{position:absolute;left:16px;top:-7px;background:#fff;padding:0 3px;font-family:"Raleway",sans-serif;font-size:7.6px;font-weight:700;line-height:11px}

/* ---------- cover panel ---------- */
.title-box{position:absolute;color:#fff;font-family:"Rajdhani",sans-serif;font-weight:700;font-size:26px;line-height:1;letter-spacing:.8px;
  display:flex;align-items:center;justify-content:center}
.title-debt{left:106px;top:88px;width:109px;height:28px;background:var(--navy)}
.title-collection{left:62px;top:121px;width:162px;height:32px;background:var(--green)}
.title-attorneys{left:94px;top:153px;width:151px;height:31px;background:var(--navy)}
.cover-name{top:490px;font-size:35px;line-height:33px;color:var(--green)}
.cover-name small{font-size:.45em;color:var(--green)}
.cover-phone{left:36px;top:581px;width:221px;height:33px;border:1.5px solid var(--ink);display:flex;align-items:center;justify-content:center;
  font-family:"Rajdhani",sans-serif;font-weight:600;font-size:27px;color:var(--ink)}
.cover-phone .icon{width:22px;height:22px;margin-right:6px}
.cover-web{left:0;top:624px;width:287px;text-align:center;font-size:11px;color:var(--body)}
.cover-web .icon{width:11px;height:11px;margin:0 3px 2px 0}
.cover-web b{color:var(--ink)}

/* ---------- inside spread ---------- */
.inside-left{left:0;top:0;width:283px;height:662px;color:#fff}
.inside-left .rule-heading{border-color:rgba(255,255,255,.5)}
.inside-left .copy{font-size:9.4px;line-height:12.9px}
.handshake{left:305px;top:90px;width:152px;height:152px;border-radius:50%;border:6px solid #fff;
  background:radial-gradient(circle at 50% 55%,#c99a7c,#e9e2da 60%,#f4f2ef)}
.col{position:absolute;color:var(--body);font-size:8.2px;line-height:10.9px}
.col p{margin-bottom:6px}
.col-heading{font-family:"Rajdhani",sans-serif;font-weight:700;font-size:15px;line-height:14px;color:var(--green);text-transform:uppercase;
  padding-left:5px;border-left:1px solid var(--green);border-bottom:1px solid var(--green);padding-bottom:1px;margin-bottom:6px}
.col-1{left:296px;top:269px;width:158px}
.col-2{left:488px;top:267px;width:156px}
.col-3{left:679px;top:269px;width:158px}
.including{font-weight:700;font-size:8.4px;margin:8px 0 4px;color:#444}
.fee-list{list-style:none;font-size:7.8px;font-weight:600;color:#444}
.fee-list li{margin-bottom:5.6px}
.fee-list li::before{content:"•";margin-right:5px}
.court-photo{width:158px;height:77px;margin:6px 0 8px;background:linear-gradient(180deg,#b9c8d9 0%,#dfe3e6 35%,#c6c7c3 70%,#8f918d 100%)}
</style>
</head>
<body>
<svg width="0" height="0" style="position:absolute" aria-hidden="true">
  <defs>
    <linearGradient id="stone" x1="0" y1="0" x2="1" y2="1">
      <stop offset="0" stop-color="#cfcfcd"/><stop offset=".45" stop-color="#eeeeec"/><stop offset="1" stop-color="#a3a4a2"/>
    </linearGradient>
    <linearGradient id="books" x1="0" y1="0" x2="1" y2="0">
      <stop offset="0" stop-color="#2a2420"/><stop offset=".5" stop-color="#6b3d22"/><stop offset="1" stop-color="#c9a574"/>
    </linearGradient>
    <linearGradient id="gavel" x1="0" y1="0" x2="1" y2="1">
      <stop offset="0" stop-color="#d8b98a"/><stop offset=".55" stop-color="#a86f45"/><stop offset="1" stop-color="#4b1f17"/>
    </linearGradient>
    <symbol id="i-phone" viewBox="0 0 24 24">
      <circle cx="12" cy="12" r="10.5" fill="none" stroke="currentColor" stroke-width="1.6"/>
      <path transform="translate(6.2 6.2) scale(.5)" fill="currentColor" d="M6.6 10.8a15 15 0 0 0 6.6 6.6l2.2-2.2a1 1 0 0 1 1-.25 11.4 11.4 0 0 0 3.6.57 1 1 0 0 1 1 1V20a1 1 0 0 1-1 1A17 17 0 0 1 3 4a1 1 0 0 1 1-1h3.5a1 1 0 0 1 1 1c0 1.25.2 2.45.57 3.57a1 1 0 0 1-.25 1z"/>
    </symbol>
    <symbol id="i-mail" viewBox="0 0 24 24">
      <circle cx="12" cy="12" r="10.5" fill="none" stroke="currentColor" stroke-width="1.8"/>
      <circle cx="12" cy="12" r="4" fill="none" stroke="currentColor" stroke-width="1.8"/>
    </symbol>
    <symbol id="i-web" viewBox="0 0 24 24">
      <circle cx="12" cy="12" r="10.5" fill="currentColor"/>
      <path d="M2 12h20M12 2c3 3 3 17 0 20M12 2c-3 3-3 17 0 20" fill="none" stroke="#fff" stroke-width="1.3"/>
    </symbol>
    <symbol id="i-pin" viewBox="0 0 24 24">
      <circle cx="12" cy="12" r="11" fill="currentColor"/>
      <path d="M12 5a4.5 4.5 0 0 0-4.5 4.5C7.5 13 12 18.5 12 18.5s4.5-5.5 4.5-9A4.5 4.5 0 0 0 12 5z" fill="#fff"/>
      <circle cx="12" cy="9.5" r="1.6" fill="currentColor"/>
    </symbol>
    <symbol id="i-tick" viewBox="0 0 24 24">
      <path d="M3 13l6 6L21 4" fill="none" stroke="#27bb93" stroke-width="3.4" stroke-linecap="round" stroke-linejoin="round"/>
    </symbol>
  </defs>
</svg>

<main class="stage">

  <!-- ================= OUTSIDE SPREAD ================= -->
  <section class="sheet sheet-outside">

    <div class="panel back-panel">
      <svg class="panel-art" viewBox="0 0 283 662" preserveAspectRatio="none" aria-hidden="true">
        <rect width="283" height="662" fill="var(--navy)"/>
        <rect y="181" width="283" height="217" fill="var(--navy-soft)"/>
      </svg>
      <h2 class="rule-heading" style="top:24px">A Trusted Partner</h2>
      <p class="copy" style="top:55px">We under the business of debt collection. Our primary focus is to help our clients secure the payments they are owed. We work closely with both private clients and leading service professionals, such as attorneys and accountants, to provide added value to their clients through customized debt collection services.</p>
      <p class="accent-line" style="top:142px">We value our relationships as trusted advisors.</p>

      <h3 class="serve-title">WE PROUDLY SERVE:</h3>
      <ul class="check-list serve-a">
        <li><svg><use href="#i-tick"/></svg>Law firms</li>
        <li><svg><use href="#i-tick"/></svg>Accounting Firms</li>
        <li><svg><use href="#i-tick"/></svg>Manufacturers</li>
        <li><svg><use href="#i-tick"/></svg>Wholesalers and Distributors</li>
        <li><svg><use href="#i-tick"/></svg>Collection Agencies</li>
        <li><svg><use href="#i-tick"/></svg>Financial Service Companies</li>
        <li><svg><use href="#i-tick"/></svg>Factors</li>
        <li><svg><use href="#i-tick"/></svg>Oil Companies</li>
      </ul>
      <ul class="check-list serve-b">
        <li><svg><use href="#i-tick"/></svg>Doctors and Healthcare Professionals</li>
        <li><svg><use href="#i-tick"/></svg>Carting Companies</li>
        <li><svg><use href="#i-tick"/></svg>Freight Forwarders &amp; Custom Brokers</li>
        <li><svg><use href="#i-tick"/></svg>Publishing and Advertising Companies</li>
        <li><svg><use href="#i-tick"/></svg>Construction and Real Estate Firms</li>
      </ul>

      <h2 class="rule-heading" style="top:410px">Why Use Us</h2>
      <ul class="check-list why-list">
        <li><svg><use href="#i-tick"/></svg>Anyone can sue a Debtor.</li>
        <li><svg><use href="#i-tick"/></svg>It's not difficult to get nasty or to treat people who owe you money in a rude and unprofessional way.</li>
        <li><svg><use href="#i-tick"/></svg>However, very few people have the skill, temperament and experience needed to effectively negotiate with Debtors, stakeholders, lawyers, as well as, court personnel, sheriffs and bankers to efficiently collect the most money possible in the least amount of time.</li>
        <li><svg><use href="#i-tick"/></svg>We truly understand the nature of commercial debt.</li>
        <li><svg><use href="#i-tick"/></svg>Collecting money is a specialized skill.</li>
      </ul>
    </div>

    <div class="panel contact-panel" style="left:283px">
      <svg class="panel-art" viewBox="0 0 287 662" preserveAspectRatio="none">
        <g role="img" aria-label="Photograph of white marble courthouse columns">
          <rect width="287" height="662" fill="url(#stone)"/>
        </g>
        <polygon points="0,440 150,510 287,450 287,662 0,662" fill="var(--paper)"/>
        <polygon points="0,181 287,316 287,425 150,505 0,440" fill="var(--green)"/>
        <polygon points="150,505 287,425 287,455 150,515" fill="var(--navy)"/>
      </svg>
      <div class="abs seal" role="img" aria-label="Photograph of bronze scales of justice"></div>
      <h1 class="abs firm-name contact-name">Arturo Dornvek<br>&amp; Company <small>PLLC</small></h1>
      <p class="abs tagline">Debt Collection Attorneys in New York State</p>
      <div class="abs hair"></div>
      <p class="abs principal">ARTURO J. DORNVEK, ESQUIRE</p>
      <p class="abs principal-role">( President )</p>
      <p class="abs reach"><svg class="icon"><use href="#i-mail"/></svg>adornvek@dornvek.com<svg class="icon"><use href="#i-phone"/></svg>(212) 555-0163</p>
      <p class="abs mail-label">MAILING ADDRESS</p>
      <p class="abs mail-lines">410 Harbor Avenue South, Suite 2210<br>New York, New York 10016-0000</p>
      <div class="abs branch">
        <p class="branch-title"><svg class="icon" style="color:var(--ink)"><use href="#i-pin"/></svg>Westchester County Office</p>
        <p class="branch-lines">150 Ridgeline Avenue, Suite 204<br>White Plains, New York 10601<br><span style="text-transform:none">(Off Exit 8 on Interstate 287)</span></p>
        <p class="branch-phones"><svg class="icon"><use href="#i-phone"/></svg>(212) 555-0148 &nbsp;<svg class="icon"><use href="#i-mail"/></svg>(917) 555-0172</p>
        <p class="branch-web"><svg class="icon" style="color:var(--ink)"><use href="#i-web"/></svg>www.<b>Dornvek</b>.com</p>
      </div>
      <div class="abs tollfree"><span class="tollfree-label">TOLL FREE</span><svg class="icon"><use href="#i-phone"/></svg>(877) 555-0190</div>
    </div>

    <div class="panel cover-panel" style="left:570px">
      <svg class="panel-art" viewBox="0 0 287 662" preserveAspectRatio="none">
        <g role="img" aria-label="Photograph of white marble courthouse columns">
          <rect width="287" height="662" fill="url(#stone)"/>
        </g>
        <polygon points="0,460 287,316 287,352 0,482" fill="var(--green)"/>
        <polygon points="0,480 287,350 287,392 0,502" fill="var(--navy)"/>
        <polygon points="0,500 287,390 287,662 0,662" fill="var(--paper)"/>
      </svg>
      <div class="title-box title-debt">DEBT</div>
      <div class="title-box title-collection">COLLECTION</div>
      <div class="title-box title-attorneys">ATTORNEYS</div>
      <h2 class="abs firm-name cover-name">Arturo Dornvek<br>&amp; Company <small>PLLC</small></h2>
      <div class="abs cover-phone"><svg class="icon"><use href="#i-phone"/></svg>(877) 555-0190</div>
      <p class="abs cover-web"><svg class="icon" style="color:var(--ink)"><use href="#i-web"/></svg>www.<b>Dornvek</b>.com</p>
    </div>
  </section>

  <!-- ================= CONTACT PANEL, SINGLE ================= -->
  <section class="sheet sheet-cover-a">
    <div class="panel contact-panel" style="left:0">
      <svg class="panel-art" viewBox="0 0 287 662" preserveAspectRatio="none">
        <g role="img" aria-label="Photograph of white marble courthouse columns">
          <rect width="287" height="662" fill="url(#stone)"/>
        </g>
        <polygon points="0,440 150,510 287,450 287,662 0,662" fill="var(--paper)"/>
        <polygon points="0,181 287,316 287,425 150,505 0,440" fill="var(--green)"/>
        <polygon points="150,505 287,425 287,455 150,515" fill="var(--navy)"/>
      </svg>
      <div class="abs seal" role="img" aria-label="Photograph of bronze scales of justice"></div>
      <h2 class="abs firm-name contact-name">Arturo Dornvek<br>&amp; Company <small>PLLC</small></h2>
      <p class="abs tagline">Debt Collection Attorneys in New York State</p>
      <div class="abs hair"></div>
      <p class="abs principal">ARTURO J. DORNVEK, ESQUIRE</p>
      <p class="abs principal-role">( President )</p>
      <p class="abs reach"><svg class="icon"><use href="#i-mail"/></svg>adornvek@dornvek.com<svg class="icon"><use href="#i-phone"/></svg>(212) 555-0163</p>
      <p class="abs mail-label">MAILING ADDRESS</p>
      <p class="abs mail-lines">410 Harbor Avenue South, Suite 2210<br>New York, New York 10016-0000</p>
      <div class="abs branch">
        <p class="branch-title"><svg class="icon" style="color:var(--ink)"><use href="#i-pin"/></svg>Westchester County Office</p>
        <p class="branch-lines">150 Ridgeline Avenue, Suite 204<br>White Plains, New York 10601<br><span style="text-transform:none">(Off Exit 8 on Interstate 287)</span></p>
        <p class="branch-phones"><svg class="icon"><use href="#i-phone"/></svg>(212) 555-0148 &nbsp;<svg class="icon"><use href="#i-mail"/></svg>(917) 555-0172</p>
        <p class="branch-web"><svg class="icon" style="color:var(--ink)"><use href="#i-web"/></svg>www.<b>Dornvek</b>.com</p>
      </div>
      <div class="abs tollfree"><span class="tollfree-label">TOLL FREE</span><svg class="icon"><use href="#i-phone"/></svg>(877) 555-0190</div>
    </div>
  </section>

  <!-- ================= INSIDE SPREAD ================= -->
  <section class="sheet sheet-inside">
    <svg class="panel-art" viewBox="0 0 857 662" preserveAspectRatio="none">
      <rect width="857" height="662" fill="var(--paper)"/>
      <rect width="283" height="662" fill="var(--navy)"/>
      <g role="img" aria-label="Photograph of a judge's gavel and brass scales on a wooden desk">
        <polygon points="270,0 857,0 857,150 630,255 283,30" fill="url(#gavel)"/>
      </g>
      <polygon points="283,30 630,255 283,262" fill="var(--navy)"/>
      <polygon points="560,258 857,150 857,195 640,262" fill="var(--green)"/>
      <g role="img" aria-label="Photograph of a shelf of leather-bound law books">
        <polygon points="0,0 283,0 283,125 0,180" fill="url(#books)"/>
      </g>
      <polygon points="0,180 283,125 283,168 0,215" fill="var(--green)"/>
      <polygon points="0,215 283,168 283,200 215,250 0,236" fill="var(--navy-deep)"/>
    </svg>

    <div class="abs handshake" role="img" aria-label="Photograph of two business people shaking hands"></div>

    <div class="abs inside-left">
      <h2 class="rule-heading" style="top:262px">Who We Are</h2>
      <p class="copy" style="top:288px">ARTURO DORNVEK &amp; COMPANY, PLLC ('DORNVEK') is a New York based law firm devoted to the collection of accounts receivable and business debts.</p>
      <h2 class="rule-heading" style="top:341px">What We Do</h2>
      <div class="copy" style="top:366px">
        <p>Within 24 to 72 hours of receiving a claim, we will verify the debt, investigate the Debtor, skip trace all known stakeholders and file a lawsuit with the intent of collecting the full amount due in the shortest time possible.</p>
        <p>We will use all legal means necessary to locate, identify, seize, or otherwise garnish a Debtor's assets and income, while always having an attorney available to speak directly with the Debtor to achieve an amicable resolution as quickly as possible.</p>
      </div>
      <h2 class="rule-heading" style="top:517px">Our Mission</h2>
      <div class="copy" style="top:543px">
        <p>Our mission is to protect our clients' bottom line, while preserving their reputation.</p>
        <p>We recognize and appreciate that your Debtor was once a trusted customer and may be a source of future revenue.</p>
        <p>We treat all Debtors with respect, while aggressively seeking to collect all monies owed.</p>
      </div>
    </div>

    <div class="col col-1">
      <h3 class="col-heading">Flexible Fee<br>Structure</h3>
      <p>We recognize that each claim is unique, therefore to better serve our clients we offer a variety of fee structures that meet the needs of our clients.</p>
      <p class="including">INCLUDING:</p>
      <ul class="fee-list">
        <li>Contingency Fee</li>
        <li>Flat Fee</li>
        <li>Hourly fee</li>
        <li>Monthly or Annual Retainer</li>
        <li>Any combination of the above</li>
      </ul>
      <h3 class="col-heading" style="margin-top:8px">Handling Medical<br>Receivables</h3>
      <p>Medical receivables require a soft touch.</p>
      <p>Doctors and health organizations often write-off tens of thousands of dollars in unpaid deductibles and co-insurance which are rightfully due them out of fear that pursuing these debts will alienate, upset or offend their patients.</p>
      <p>We offer non-legal, HIPAA compliant collection methods which can effectively and consistently turn these otherwise uncollectible assets into real cash.</p>
    </div>

    <div class="col col-2">
      <p>Using a combination of letters and phone calls, our staff contacts patients in a professional and friendly manner to arrange for payments, as small as $15 per month, encouraging them to pay all monies owed.</p>
      <h3 class="col-heading">Credit Advisory<br>Services</h3>
      <p>How well do you really know your customers?</p>
      <p>As an added service to all of our clients, we will draft a customized credit application to be distributed to all of their customers.</p>
      <p>Working closely and alongside their salespeople, we will discreetly review and verify the customers' information and investigate all known stakeholders in order to determine creditworthiness.</p>
      <p>As your credit advisor, we will then make a meaningful recommendation with regard to the amount and terms credit should be offered to specific customers.</p>
      <p>Once a credit determination is made, we can provide the client with a credit agreement detailing each</p>
      <p>parties' obligations. Using such agreements minimizes risk, while enhancing our clients' professional stature with their customers.</p>
    </div>

    <div class="col col-3">
      <h3 class="col-heading">Keeping You In<br>Compliance</h3>
      <p>As your collection attorney and advisor, we will assure that your collection practices are in full compliance with all applicable Federal and State laws, including The Fair Debt Collection Practices Act (FDCPA) and The Health Insurance Portability and Accountability Act (HIPPA).</p>
      <div class="court-photo" role="img" aria-label="Photograph of a columned courthouse facade"></div>
      <h3 class="col-heading">State-of-the Art<br>Technology</h3>
      <p>Our firm prides itself on utilizing the state-of-the-art technology in law office management, telephony, cyber security, document production, and cloud storage.</p>
      <p>Our clients can be assured that their critical business data is stored in a safe, secure, and confidential environment, while allowing us to seamlessly handle a large and ever growing book of business in a timely manner.</p>
    </div>
  </section>

  <!-- ================= COVER PANEL, SINGLE ================= -->
  <section class="sheet sheet-cover-b">
    <div class="panel cover-panel" style="left:0">
      <svg class="panel-art" viewBox="0 0 287 662" preserveAspectRatio="none">
        <g role="img" aria-label="Photograph of white marble courthouse columns">
          <rect width="287" height="662" fill="url(#stone)"/>
        </g>
        <polygon points="0,330 287,315 287,352 0,392" fill="var(--green)"/>
        <polygon points="0,390 287,350 287,395 0,470" fill="var(--navy)"/>
        <polygon points="0,468 287,393 287,662 0,662" fill="var(--paper)"/>
      </svg>
      <div class="title-box title-debt">DEBT</div>
      <div class="title-box title-collection">COLLECTION</div>
      <div class="title-box title-attorneys">ATTORNEYS</div>
      <h2 class="abs firm-name cover-name">Arturo Dornvek<br>&amp; Company <small>PLLC</small></h2>
      <div class="abs cover-phone"><svg class="icon"><use href="#i-phone"/></svg>(877) 555-0190</div>
      <p class="abs cover-web"><svg class="icon" style="color:var(--ink)"><use href="#i-web"/></svg>www.<b>Dornvek</b>.com</p>
    </div>
  </section>

</main>
</body>
</html>
```